Personal coach needs brochure design for inspirational essay about authenticity

Overview:
I want a beautiful brochure, 11”x17” that folds to 8-1/2”x11” with 4 pages. Think of it as an oversize greeting card.
• Front cover: photograph of a dancer and title with attribution of quote (Lumafold jpeg photo attached)
• Inside spread: Copy (Helena Brisk copy attached) with some appropriate illustration, based on cover photo
• Back cover: contact information, brief descriptive copy, two small photos (jpeg photo attached; see copy for direction)
Copy for front cover title, inside spread and back cover is attached in doc titled "Helena Brisk copy"

Purpose of brochure:
I'm a personal coach and once a year I produce a 4-page illustrated inspirational essay, which invites personal reflection on living a more mindful, meaningful life. Most people I send them to collect them. Someday in the future I'd like to put a collection of these essays into a coffee table book and also create a website for the collection, which is related to the personal coaching that I do.
I have the brochures printed hard copy. I have attached a few examples from previous years. Each has a unique design related to its theme.

Concept:
This year’s essay theme, “There will only ever be one you!” is based on a quote by Helena Brisk, a famous modern dancer. The complete quote, which appears in the copy, is about being true to one’s authentic self. The essay is not about dance, but because the author of the quote was a dancer who personified this theme of being unique to self, I have selected a photo of dance for the cover.

Design Guidance:
Front cover: One possibility is to expand the background color of the Lumafold photo so the photo seems to emerge from the background. But I am open to ideas. I think the photo is artsy enough as it is, but there may be other ways to treat it (e.g. special effects) that would also work. The title should appear somewhere. Make the attribution (--Helena Brisk) in smaller type than the title.

Inside Spread: There may be ways to borrow a design motif from the cover photo to make the inside spread more visually interesting, i.e., not just straight copy. I think it may be helpful to make the font size of the quote larger than the rest of the copy, but it has to be read in sequence. Or maybe it's printed in same size as copy, but then also repeated and displayed by itself in larger type.

Back cover: If you look at some of the other examples I’ve sent, you’ll see how the back cover is typically handled. I want a reduced version of the cover to be placed near the line that says "this is the 16th in a series.." Then, there’s a jpeg photo of Helena Brisk that should be placed next to the copy description of her.

Need extra days to review

```html
<!DOCTYPE html>
<html lang="en">
<head>
<meta charset="utf-8">
<title>There Will Only Ever Be One You — Essay Brochure</title>
<link rel="stylesheet" href="https://fonts.googleapis.com/css2?family=Raleway:ital,wght@0,300;0,400;0,600;0,700;1,600&family=Open+Sans:wght@400;600&display=swap">
<style>
  :root {
    --canvas: #e4e4e6;
    --paper: #ffffff;
    --paper-grey: #d3d3d3;
    --band-grey: #b9b9b9;
    --ink: #2a2a2a;
    --ink-soft: #555555;
    --night: #141719;
    --smoke: #5b6468;
    --mist: #8c979b;
    --white: #ffffff;
  }
  * { box-sizing: border-box; margin: 0; padding: 0; }
  html, body { width: 1200px; height: 1000px; overflow: hidden; }
  body {
    background: var(--canvas);
    font-family: "Open Sans", Arial, sans-serif;
    color: var(--ink);
    position: relative;
  }
  .spread {
    position: absolute;
    left: 230px;
    width: 740px;
    height: 479px;
    display: flex;
    box-shadow: 0 6px 18px rgba(0,0,0,0.18);
  }
  .spread--outer { top: 12px; }
  .spread--inner { top: 508px; }
  .page { position: relative; width: 370px; height: 100%; overflow: hidden; }

  /* Back cover */
  .back-cover { display: flex; background: var(--paper); }
  .back-cover__rail { width: 118px; background: var(--paper-grey); position: relative; }
  .back-cover__body { flex: 1; padding: 22px 16px 16px 14px; font-size: 5.6px; line-height: 1.45; }
  .thumb { position: absolute; left: 22px; width: 78px; }
  .thumb--cover {
    top: 20px; height: 62px;
    background: radial-gradient(ellipse at 55% 45%, var(--mist) 0%, var(--smoke) 35%, var(--night) 85%);
  }
  .thumb--portrait {
    top: 222px; height: 66px;
    background: radial-gradient(ellipse at 50% 50%, #b9ab94 0%, #5a5046 30%, #120f0d 75%);
  }
  .thumb-caption {
    position: absolute; left: 14px; top: 293px; width: 94px;
    font-size: 4.6px; line-height: 1.4; color: var(--ink-soft);
  }
  .series-note { margin-bottom: 30px; }
  .series-note b { font-family: "Raleway", Arial, sans-serif; font-weight: 700; font-style: italic; }
  .contact { margin-bottom: 8px; color: var(--ink-soft); }
  .contact p + p { margin-top: 7px; }
  .copyright { margin: 10px 0 30px; color: var(--ink-soft); }
  .about { margin-bottom: 9px; text-align: justify; }
  .about__lead {
    font-family: "Raleway", Arial, sans-serif; font-weight: 700; font-size: 6.4px;
  }
  .about__lead::first-letter { font-size: 15px; float: left; line-height: 1; margin-right: 2px; }

  /* Front cover */
  .front-cover__photo {
    position: absolute; inset: 0;
    background:
      radial-gradient(ellipse at 58% 26%, #9aa6a9 0%, #66716f 22%, transparent 48%),
      radial-gradient(ellipse at 40% 70%, #4a5254 0%, transparent 55%),
      linear-gradient(170deg, #2c3234 0%, #1a1e20 55%, #0e1011 100%);
  }
  .front-cover__title {
    position: absolute; right: 26px; bottom: 62px;
    font-family: "Raleway", Arial, sans-serif; font-weight: 300;
    font-size: 38px; line-height: 0.98; letter-spacing: -0.5px;
    color: var(--white); text-align: right;
  }
  .front-cover__credit {
    position: absolute; right: 40px; bottom: 40px;
    font-family: "Raleway", Arial, sans-serif; font-weight: 300; font-size: 12px;
    color: var(--white); letter-spacing: 0.6px;
  }

  /* Inside spread */
  .inner-left { background: var(--paper); }
  .inner-right { background: var(--paper); }
  .inner-right__band { position: absolute; left: 0; top: 0; width: 100%; height: 228px; background: var(--band-grey); }
  .inner-right__rule { position: absolute; left: 0; top: 228px; width: 100%; height: 3px; background: var(--paper); }
  .columns {
    position: absolute; top: 24px; display: flex; gap: 16px;
    font-size: 5.6px; line-height: 1.5; text-align: justify;
  }
  .inner-left .columns { left: 30px; right: 24px; }
  .inner-right .columns { left: 22px; right: 30px; }
  .columns .col { flex: 1; }
  .columns p + p { margin-top: 7px; }
  .drop::first-letter {
    font-family: "Raleway", Arial, sans-serif; font-weight: 700;
    font-size: 20px; float: left; line-height: 0.9; margin-right: 2px;
  }
  .quote-band {
    position: absolute; left: 230px; top: 742px; width: 740px; height: 245px;
    background:
      radial-gradient(ellipse at 30% 40%, #3e4648 0%, transparent 50%),
      radial-gradient(ellipse at 75% 70%, #363d3f 0%, transparent 45%),
      linear-gradient(180deg, #23282a 0%, #131617 100%);
  }
  .quote-band__text {
    position: absolute; left: 268px; top: 770px; width: 660px;
    font-family: "Raleway", Arial, sans-serif; font-weight: 300;
    font-size: 13.4px; line-height: 1.42; color: var(--white);
  }
  .quote-band__mark {
    position: absolute; left: 244px; top: 758px;
    font-family: "Raleway", Arial, sans-serif; font-weight: 700;
    font-size: 44px; line-height: 1; color: var(--white);
  }
</style>
</head>
<body>

<!-- Outer spread: back cover and front cover -->
<section class="spread spread--outer">
  <article class="page back-cover">
    <div class="back-cover__rail">
      <div class="thumb thumb--cover" role="img" aria-label="Reduced front cover: dancer leaping through dark smoke"></div>
      <div class="thumb thumb--portrait" role="img" aria-label="Photo of Helena Brisk dancing in a flowing pale gown on a dark stage"></div>
      <p class="thumb-caption">Helena Brisk in Letter to the Sky, 1940. Photo by Ruth Calloway.</p>
    </div>
    <div class="back-cover__body">
      <p class="series-note"><b>There Will Only Ever Be One You</b> is the 16th in a series of Labor Day essays inviting a moment of reflection on living a more meaningful, more mindful life.</p>
      <div class="contact">
        <p>Dana Ellory, Ph.D.<br>Willow Bend House<br>18 Orchard Lane<br>Fairhaven, Vermont 05743</p>
        <p>555-013-2846</p>
        <p>d.ellory@mailpost.example</p>
      </div>
      <p class="copyright">©2023</p>
      <p class="about"><span class="about__lead">About Helena Brisk:</span> Born in 1894, Helena Brisk danced and taught for over 70 years. She is recognized as a pioneer of modern dance whose work explored the full range of human emotion, drawing on myth, memory and the landscape of her country to create a bold new language of movement.</p>
      <p class="about"><span class="about__lead">About Photographer Ruth Calloway:</span> In 1935 Ruth Calloway began photographing modern dancers, capturing the energy of each gesture in a single frame. Her portraits of Brisk remain among the most celebrated images of the era, and this photo shows her in a solo inspired by the poetry of Iris Harlow.</p>
    </div>
  </article>

  <article class="page front-cover">
    <div class="front-cover__photo" role="img" aria-label="Photograph of a dancer in a flowing dark dress leaping through swirling grey smoke"></div>
    <h1 class="front-cover__title">There will<br>only ever be<br>one you!</h1>
    <p class="front-cover__credit">Helena Brisk</p>
  </article>
</section>

<!-- Inside spread -->
<section class="spread spread--inner">
  <article class="page inner-left">
    <div class="columns">
      <div class="col">
        <p class="drop">In the rural Ohio village where I grew up, one of the highlights of Sunday morning church service was the anthem sung by the choir. Week after week I waited for the special voice of one soprano whose sound rose above the rest and filled the small chapel with light.</p>
        <p>Despite the reverence of my pew, I could not help noticing how she never tried to blend in. Her voice was simply hers, and that was the gift.</p>
      </div>
      <div class="col">
        <p>Years later I came to see that each of us carries a voice like hers. Some of us hide it, afraid it is not good enough, while others let it ring out without apology.</p>
        <p>Someone who understood this was the dancer Helena Brisk, who believed every person holds something no one else can offer.</p>
      </div>
    </div>
  </article>

  <article class="page inner-right">
    <div class="inner-right__band"></div>
    <div class="inner-right__rule"></div>
    <div class="columns">
      <div class="col">
        <p>In her biography of Brisk, her friend and equally talented choreographer Clara Vane recalled that despite sensational reviews for her own innovative work, Vane had a growing feeling that her work was only mediocre. She confessed her anxieties to Brisk, who responded: “There will only ever be one you.” Continuing, she added:</p>
        <p>“There is a vitality, a life force, an energy, a quickening that is translated through you into action. And because there is only one of you in all of time, this expression is unique. And if you block it, the world will not have it. It is not your business to determine how good it is nor how valuable nor how it compares with other expressions. It is your business to keep it yours clearly and directly, to keep the channel open. You have to</p>
      </div>
      <div class="col">
        <p>keep open and aware directly to the urges that motivate you. Above all else, keep the channel open!”</p>
        <p>Brisk’s wisdom reminds us that we must not hold back or judge our gifts. Although there may be moments when we doubt ourselves or when we worry that we’re not good enough, our job is to be fearless and to “keep the channel open.”</p>
        <p>Guard the precious miracle of your own uniqueness. Find that home sweet home feeling where you feel you are your most authentic self. There will only ever be one you! And importantly, respect the differences of others. Our world would be a drab, boring place if we all only sang one tune.</p>
      </div>
    </div>
  </article>
</section>

<div class="quote-band" role="img" aria-label="Dark textured band of swirling grey smoke echoing the cover photograph"></div>
<span class="quote-band__mark" aria-hidden="true">“</span>
<blockquote class="quote-band__text">There is a vitality, a life force, an energy, a quickening that is translated through you into action. And because there is only one of you in all of time, this expression is unique. And if you block it, the world will not have it. It is not your business to determine how good it is nor how valuable nor how it compares with other expressions. It is your business to keep it yours clearly and directly, to keep the channel open. You have to keep open and aware directly to the urges that motivate you. Above all else, keep the channel open!</blockquote>

</body>
</html>
```